A new medical waste company needs an attractive and modern flyer.

We are a new medical waste company disposing of biohazards waste, red bag waste and sharps disposal with a focus on customer service.

Background Information

Company Name
Korvane Waste

Industry
Medical waste management

Description of the organization and its target audience

We are a new medical waste company disposing of biohazardous waste, red bag waste and medical sharps.

Description

MODERN & ELEGANT HALF PAGE FLYER

Half page mailer (front and back) with a large image related to the medical field.

The Korvane Waste logo, with the company tag line “compliant waste solutions” should also be on front of the mailer.

Website (korvanewaste.example) & email (info@korvanewsate.example) on both sides of the flyer

Main headline
-Now you have options for your medical waste disposal

Who we serve
- Dentist
- Physicians
-Blood banks
-Tattoo parlors
-Assisted living facilities
-Laboratories
-Veterinarians

What we offer
-Straight forward pricing
-No hidden fees
-No long term contracts
-Free containers and red bags
-Routine scheduled pickups

Price $35.95
Updates

Remember this is a half page flyer. Please remove pricing from all future work.

Target Market(s)

- Dentist
- Physicians
-Blood banks
-Tattoo parlors
-Laboratories
-Veterinarians

Industry/Entity Type

It Company

Colors
33b8a4

Requirements
Must have
• See my website www.korvanewaste.example

```html
<!DOCTYPE html>
<html lang="en">
<head>
<meta charset="utf-8">
<title>Korvane Waste – Half Page Flyer</title>
<link href="https://fonts.googleapis.com/css2?family=Lato:wght@400;700;900&display=swap" rel="stylesheet">
<style>
  :root {
    --teal: #33b8a4;
    --teal-bright: #2fc2b8;
    --teal-soft: #4fb7b0;
    --navy: #1b3a4c;
    --navy-band: #1f4858;
    --ink: #173445;
    --white: #ffffff;
    --backdrop: #e4e4e4;
  }
  * { box-sizing: border-box; margin: 0; padding: 0; }
  html, body { width: 1200px; height: 800px; overflow: hidden; }
  body {
    background: var(--backdrop);
    font-family: "Lato", Arial, sans-serif;
    position: relative;
  }
  .flyer {
    position: absolute;
    top: 60px;
    width: 440px;
    height: 680px;
    overflow: hidden;
    background: var(--teal);
    box-shadow: 0 6px 18px rgba(0,0,0,0.18);
  }
  .flyer--front { left: 120px; }
  .flyer--back { left: 640px; background: linear-gradient(180deg, var(--teal-bright), var(--teal)); }

  /* front */
  .hero-photo {
    position: absolute; left: 0; top: 0; width: 100%; height: 420px;
    background: linear-gradient(160deg, #9fb3cc 0%, #5f7fb5 40%, #3d5fa4 70%, #6b87b8 100%);
  }
  .brand-panel {
    position: absolute; left: 0; top: 36px; width: 270px; height: 112px;
    background: rgba(27,58,76,0.88);
    padding: 18px 18px 0 20px;
  }
  .brand {
    display: flex; align-items: center; gap: 10px;
    color: var(--teal-bright); font-weight: 700; font-size: 24px; letter-spacing: 0.5px;
  }
  .brand-dot {
    width: 30px; height: 30px; border-radius: 50%; background: var(--teal); flex: none;
  }
  .tagline {
    margin-top: 16px; color: var(--white); font-weight: 700; font-size: 16px;
  }
  .headline-band {
    position: absolute; left: 0; top: 420px; width: 100%; height: 108px;
    background: var(--navy-band);
    padding: 18px 22px;
    color: var(--white); font-weight: 900; font-size: 28px; line-height: 1.2;
  }
  .intro-band {
    position: absolute; left: 0; top: 528px; width: 100%; height: 106px;
    padding: 14px 22px 0;
    color: var(--ink); font-weight: 700; font-size: 19px; line-height: 1.2;
  }
  .intro-email {
    position: absolute; right: 20px; bottom: 8px;
    display: flex; align-items: center; gap: 6px; font-size: 15px;
  }
  .footer-band {
    position: absolute; left: 0; bottom: 0; width: 100%; height: 46px;
    background: var(--navy);
    display: flex; align-items: center; gap: 8px; padding: 0 22px;
    color: var(--white); font-weight: 700; font-size: 17px;
  }
  .icon { width: 18px; height: 18px; flex: none; }

  /* back */
  .back-header {
    position: absolute; left: 0; top: 0; width: 100%; height: 96px;
    background: var(--navy-band);
    display: flex; align-items: center; justify-content: flex-end; padding-right: 30px;
  }
  .side-photo {
    position: absolute; left: 0; top: 0; width: 150px; height: 634px;
    background: linear-gradient(180deg, rgba(120,150,165,0.55), rgba(60,150,150,0.5) 50%, rgba(140,140,110,0.45));
  }
  .back-content {
    position: absolute; left: 175px; top: 120px; right: 16px;
    color: var(--ink); font-weight: 700;
  }
  .section-label {
    display: inline-block; background: var(--teal-soft);
    color: var(--white); font-size: 17px; padding: 4px 10px; margin-bottom: 12px;
  }
  .offer-list { list-style: none; font-size: 18px; line-height: 1.22; margin-bottom: 18px; }
  .offer-list li::before { content: "- "; }
  .back-footer {
    position: absolute; left: 0; bottom: 0; width: 100%; height: 46px;
    background: var(--navy);
    display: flex; align-items: center; justify-content: space-between; padding: 0 18px;
    color: var(--white); font-weight: 700; font-size: 15px;
  }
  .contact { display: flex; align-items: center; gap: 6px; }
</style>
</head>
<body>

<section class="flyer flyer--front">
  <div class="hero-photo" role="img" aria-label="Photo of surgical staff in scrubs and caps working in an operating room"></div>
  <div class="brand-panel">
    <div class="brand"><span class="brand-dot"></span>Korvane Waste</div>
    <p class="tagline">compliant waste solutions</p>
  </div>
  <h1 class="headline-band">Now you have options for your medical waste disposal</h1>
  <div class="intro-band">
    <p>We are a new medical waste company disposing of biohazardous waste, red bag waste and medical sharps</p>
    <span class="intro-email">
      <svg class="icon" viewBox="0 0 20 20"><rect x="1" y="4" width="18" height="12" fill="none" stroke="#173445" stroke-width="2"/><path d="M1 4 L10 11 L19 4" fill="none" stroke="#173445" stroke-width="2"/></svg>
      info@korvanewsate.example
    </span>
  </div>
  <footer class="footer-band">
    <svg class="icon" viewBox="0 0 20 20"><circle cx="10" cy="10" r="9" fill="var(--teal)"/><path d="M4 7c3 0 4 2 3 4s1 4 0 6M13 3c-1 3 2 4 4 4" fill="none" stroke="#1b3a4c" stroke-width="1.6"/></svg>
    korvanewaste.example
  </footer>
</section>

<section class="flyer flyer--back">
  <div class="side-photo" role="img" aria-label="Faded close-up photo of medical equipment under a teal tint"></div>
  <header class="back-header">
    <div class="brand"><span class="brand-dot"></span>Korvane Waste</div>
  </header>
  <div class="back-content">
    <h2 class="section-label">Who we serve</h2>
    <ul class="offer-list">
      <li>Dentist</li>
      <li>Physicians</li>
      <li>Blood banks</li>
      <li>Tattoo parlors</li>
      <li>Assisted living facilities</li>
      <li>Laboratories</li>
      <li>Veterinarians</li>
    </ul>
    <h2 class="section-label">What we offer</h2>
    <ul class="offer-list">
      <li>Straight forward pricing</li>
      <li>No hidden fees</li>
      <li>No long term contracts</li>
      <li>Free containers and red bags</li>
      <li>Routine scheduled pickups</li>
    </ul>
  </div>
  <footer class="back-footer">
    <span class="contact">
      <svg class="icon" viewBox="0 0 20 20"><circle cx="10" cy="10" r="9" fill="var(--teal)"/><path d="M4 7c3 0 4 2 3 4s1 4 0 6M13 3c-1 3 2 4 4 4" fill="none" stroke="#1b3a4c" stroke-width="1.6"/></svg>
      korvanewaste.example
    </span>
    <span class="contact">
      <svg class="icon" viewBox="0 0 20 20"><rect x="1" y="4" width="18" height="12" fill="none" stroke="#33b8a4" stroke-width="2"/><path d="M1 4 L10 11 L19 4" fill="none" stroke="#33b8a4" stroke-width="2"/></svg>
      info@korvanewsate.example
    </span>
  </footer>
</section>

</body>
</html>
```